Bluecrest Ore Company needs a company newsletter template

We need a 2-page editable newsletter template, that we can update monthly with various information and pictures. We would like an area to include our values: Be Safe, Be Honest, Be Responsible, Be Respectful, Be Great. Ideally we would have 2-3 bulk text areas to highlight different things each month, with area we an update a picture from time to time and maybe some text areas where we can add a fun fact type thing. Some of the areas we will include are production milestones (if any), monthly tenure, monthly new hires, highlighting an employee that demonstrates our value, community engagement, upcoming holidays/events, press releases. The exact content will likely change month to month but these will be some of the frequent topics. We are a copper Mine in northern Yukon. I've attached our Brand Guidelines and logo files. Our website is ravelorex.com if you want to see the style and type of photos from our site

```html
<!DOCTYPE html>
<html lang="en">
<head>
<meta charset="utf-8">
<title>Bluecrest Matters Newsletter</title>
<link rel="stylesheet" href="https://fonts.googleapis.com/css2?family=Montserrat:wght@800&family=Roboto:wght@400;500;700;900&display=swap">
<style>
:root{
  --bg:#e9ebef;
  --paper:#ffffff;
  --navy:#1f2a44;
  --brown:#7b3a22;
  --rust:#a4614a;
  --rust-dark:#8a4632;
  --gold:#f3bf3d;
  --gold-soft:#f6cf60;
  --ink:#2a2a2a;
  --grey:#e6e7e8;
  --grey-2:#d9dddd;
}
*{margin:0;padding:0;box-sizing:border-box}
html,body{width:1200px;height:2578px;overflow:hidden}
body{background:var(--bg);font-family:"Roboto",Arial,sans-serif;color:var(--ink);position:relative}
.page{position:absolute;left:193px;width:813px;height:1052px;background:var(--paper);box-shadow:0 6px 18px rgba(0,0,0,.18);overflow:hidden}
.page-one{top:177px}
.page-two{top:1348px}
.abs{position:absolute}

/* masthead */
.brand-mark{left:70px;top:52px;width:60px;height:60px;background:var(--gold);border-radius:50%}
.brand-name{left:36px;top:122px;font-size:14px;font-weight:700;color:var(--brown);letter-spacing:.2px;white-space:nowrap}
.masthead-title{left:248px;top:48px;font-family:"Montserrat",sans-serif;font-weight:800;font-size:38px;line-height:1;color:var(--navy);letter-spacing:-.5px;white-space:nowrap}
.masthead-title span{color:var(--brown)}
.masthead-sub{left:248px;top:98px;font-size:60px;font-weight:500;color:var(--brown);letter-spacing:-1px;line-height:1;white-space:nowrap}

/* hero */
.hero{left:43px;top:174px;width:727px;height:233px;overflow:hidden}
.hero svg{position:absolute;left:0;top:0}
.hero-heading{left:29px;top:35px;font-size:22px;font-weight:500;color:var(--navy)}
.hero-text{left:29px;top:70px;width:260px;font-size:13.5px;line-height:16.7px;color:#3b2a1e}
.intro-text{left:44px;top:424px;width:726px;font-size:10.4px;line-height:12.8px;color:#222}

/* values */
.values{left:43px;top:520px;width:314px;height:296px;background:var(--rust)}
.values-head{left:20px;top:18px;width:257px;height:38px;border-bottom:2px solid #f0e0d8;display:flex;align-items:center;gap:16px}
.values-head h2{font-size:23px;font-weight:400;color:#fff}
.values-head h2 b{font-weight:700}
.value-row{left:21px;display:flex;align-items:center;gap:18px}
.value-icon{width:36px;height:34px;background:var(--gold);display:flex;align-items:center;justify-content:center}
.value-row span{font-size:21px;color:#fff;font-weight:400}
.value-row span b{font-weight:700}

/* fun fact */
.fact{left:43px;top:842px;width:314px;height:164px;background:var(--gold)}
.fact-bar{left:0;top:0;width:314px;height:28px;background:var(--rust-dark);color:#fff;font-size:18px;font-weight:700;text-align:center;line-height:28px}
.fact-badge{left:22px;top:58px;width:98px;height:84px;background:#5a4a3a;border-radius:48% 52% 44% 56%;color:#fff;font-weight:900;font-size:25px;line-height:22px;text-align:center;padding-top:18px}
.fact-list{left:134px;top:50px;width:170px;list-style:none}
.fact-list li{font-size:9.5px;line-height:11px;color:#4a3020;padding-left:14px;position:relative;margin-bottom:11px}
.fact-list li::before{content:"";position:absolute;left:0;top:3px;width:8px;height:8px;border-radius:50%;background:var(--rust)}

/* outlook */
.outlook-title{left:393px;top:514px;font-size:25px;font-weight:400;color:var(--navy)}
.outlook-title b{color:var(--rust);font-weight:700}
.outlook-row{left:393px;width:377px;height:62px;border-bottom:2px solid var(--gold)}
.date-box{position:absolute;left:0;top:3px;width:70px;height:50px;background:var(--navy);color:var(--gold);font-size:21px;font-weight:700;line-height:20px;text-align:center;padding-top:5px}
.outlook-row p{position:absolute;left:84px;top:1px;width:285px;font-size:10.4px;line-height:12.8px;color:#333}

/* employee */
.employee{left:393px;top:771px;width:377px;height:235px;background:var(--gold)}
.employee-bar{left:0;top:0;width:377px;height:35px;background:var(--rust-dark);color:#fff;font-size:19px;font-weight:700;line-height:36px;padding-left:17px}
.employee-photo{left:11px;top:46px;width:140px;height:178px}
.employee-card{left:163px;top:46px;width:202px;height:178px;background:var(--rust)}
.employee-card h3{position:absolute;left:14px;top:10px;font-size:17px;color:var(--gold);font-weight:700}
.employee-card p{position:absolute;left:16px;top:36px;width:175px;font-size:10.6px;line-height:12.8px;color:#fff}

/* page two */
.gm{left:43px;top:42px;width:394px;height:400px}
.gm-title{left:80px;top:83px;font-size:53px;color:#fff;font-weight:400;letter-spacing:-.5px}
.gm-title b{font-weight:900}
.gm-rule{left:82px;top:172px;width:6px;height:182px;background:var(--gold)}
.gm-text{left:101px;top:168px;width:205px;font-size:10.6px;line-height:14.7px;color:#fff}

.side-title{font-size:18px;color:#333;font-weight:400}
.side-title b{color:var(--rust);font-weight:500}
.roster{list-style:none}
.roster li{height:15.5px;font-size:9.5px;font-weight:700;color:#333;padding-left:24px;line-height:15.5px;position:relative}
.roster li::before{content:"";position:absolute;left:10px;top:4px;width:7px;height:7px;border-radius:50%;background:#fff}
.tenure{left:469px;top:67px;width:301px}
.tenure li:nth-child(odd){background:var(--gold)}
.tenure li:nth-child(even){background:var(--gold-soft)}
.hires{left:469px;top:279px;width:301px}
.hires li:nth-child(odd){background:#ececec}
.hires li:nth-child(even){background:#f7f7f7}
.hires li{font-weight:500}
.hires li::before{background:#8a8a8a;width:5px;height:5px;top:5px}
.hires-img{left:645px;top:285px;width:110px;height:150px}

.wellness{left:44px;top:460px;width:393px;height:170px;background:var(--grey)}
.wellness h2{position:absolute;left:20px;top:8px;font-size:24px;font-weight:400;color:#333}
.wellness h2 b{color:var(--rust);font-weight:700}
.wellness .rule{position:absolute;left:20px;top:40px;width:348px;height:2px;background:var(--gold)}
.wellness p{position:absolute;left:20px;width:350px;font-size:10.4px;line-height:12.8px;color:#333}

.hiring{left:467px;top:458px;width:301px;height:172px;background:var(--grey-2)}
.hiring h2{position:absolute;left:14px;top:16px;font-size:24px;line-height:24px;color:var(--navy);font-weight:500}
.hiring h2 b{display:block;color:var(--rust);font-size:31px;font-weight:700}
.hiring ul{position:absolute;left:14px;top:84px;list-style:none;z-index:1}
.hiring li{font-size:10.4px;color:#333;padding-left:13px;position:relative;margin-bottom:6px}
.hiring li::before{content:"";position:absolute;left:0;top:3px;width:7px;height:7px;border-radius:50%;background:var(--rust)}
.hiring-img{left:192px;top:10px;width:106px;height:150px}

.col-title{font-size:18px;color:#333;font-weight:400;white-space:nowrap}
.col-title b{color:var(--rust);font-weight:500}
.col-rule{height:2px;background:var(--gold)}
.col-date{font-size:12px;font-weight:500;color:var(--rust)}
.col-date i{display:inline-block;margin-left:10px;width:10px;height:10px;border-left:2px solid var(--gold);border-right:2px solid var(--gold);vertical-align:-1px}
.col-list{list-style:none}
.col-list li{font-size:10.4px;line-height:12.8px;color:#333;padding-left:16px;position:relative;margin-bottom:4px}
.col-list li::before{content:"";position:absolute;left:2px;top:3px;width:7px;height:7px;border-radius:50%;background:var(--rust)}
.holiday-box{left:290px;top:684px;width:236px;height:88px;background:var(--rust)}
.holiday-box .col-date{color:#fff;position:absolute;left:12px;top:8px}
.holiday-box .col-list{position:absolute;left:12px;top:28px}
.holiday-box li{color:var(--gold);font-weight:500;margin-bottom:4px}
.holiday-box li::before{background:var(--gold)}

.strip{left:43px;top:792px;width:727px;height:168px;overflow:hidden}
.strip svg{position:absolute;left:0;top:0}
.strip-title{left:405px;top:30px;color:var(--navy);font-size:14px;font-weight:700;line-height:15px}
.strip-title b{display:block;font-size:23px;font-weight:900;line-height:22px}
.cal{width:96px;height:72px;background:#fff;border-radius:6px;overflow:hidden}
.cal h4{font-size:9px;font-weight:700;text-align:center;height:12px;line-height:12px;letter-spacing:.5px;color:var(--navy);background:#f2e6d4}
.cal.dark h4{background:var(--rust-dark);color:#fff}
.cal .grid{display:grid;grid-template-columns:repeat(7,1fr);padding:3px 6px 0;font-size:4.6px;line-height:7.3px;text-align:center;color:#333}
.cal .grid span:nth-child(-n+7){font-weight:700}

.footer{left:0;top:972px;width:813px;height:80px;background:var(--rust-dark)}
.footer-globe{left:47px;top:23px;width:34px;height:34px;border-radius:8px;background:var(--gold);display:flex;align-items:center;justify-content:center}
.footer-url{left:93px;top:27px;font-size:18px;font-weight:500;color:#fff}
.footer-follow{left:610px;top:27px;font-size:18px;font-weight:500;color:#fff}
.social{top:31px;width:17px;height:17px;border-radius:50%;background:var(--gold)}
</style>
</head>
<body>

<section class="page page-one">
  <div class="abs brand-mark"></div>
  <div class="abs brand-name">BLUECREST ORE COMPANY</div>
  <h1 class="abs masthead-title">BLUECREST <span>MATTERS</span></h1>
  <div class="abs masthead-sub">NEWS LETTER</div>

  <div class="abs hero">
    <svg width="727" height="233" viewBox="0 0 727 233">
      <defs>
        <linearGradient id="heroGold" x1="0" y1="0" x2="0" y2="1">
          <stop offset="0" stop-color="#f5d35c"/><stop offset="1" stop-color="#f3a323"/>
        </linearGradient>
        <linearGradient id="heroScene" x1="0" y1="0" x2="0" y2="1">
          <stop offset="0" stop-color="#c9c5b6"/><stop offset=".35" stop-color="#8a8f8c"/><stop offset=".6" stop-color="#7a7c8c"/><stop offset="1" stop-color="#9c5034"/>
        </linearGradient>
      </defs>
      <rect width="727" height="233" fill="url(#heroGold)"/>
      <polygon points="390,0 727,0 727,233 272,233" fill="url(#heroScene)" role="img" aria-label="Aerial photo of a river valley in the north"/>
    </svg>
    <h2 class="abs hero-heading">DEPARTMENT</h2>
    <p class="abs hero-text">Lorem ipsum dolor sit amet, consectetur adipiscing elit, sed do eiusmod tempor incididunt ut labore et dolore magna aliqua. Quis ipsum suspendisse ultrices gravida. Risus commodo viverra maecenas accumsan lacus vel facilisis. Lorem ipsum dolor sit amet.</p>
  </div>

  <p class="abs intro-text">Lorem Ipsum is simply dummy text of the printing and typesetting industry. Lorem Ipsum has been the industry's standard dummy text ever since the 1500s, when an unknown printer took a galley of type and scrambled it to make a type specimen book. Lorem Ipsum is simply dummy text of the printing and typesetting industry. Lorem Ipsum has been the industry's standard dummy text ever since the 1500s, when an unknown printer took a galley of typeLorem Ipsum is simply dummy text of the printing and typesetting industry. Lorem Ipsum has been the industry's standard dummy text ever since the 1500s, when an unknown printer took a galley of type and scrambled it to make a type specimen book. Lorem Ipsum is simply dummy text of the printing and typesetting industry. Lorem Ipsum has been the industry's standard dummy text ever since the 1500s, when an unknown printer took a galley of type.</p>

  <div class="abs values">
    <div class="abs values-head">
      <svg width="44" height="34" viewBox="0 0 44 34" fill="none" stroke="#fff" stroke-width="1.6"><rect x="4" y="3" width="14" height="10" rx="1"/><path d="M22 18h18M31 18v12M24 30h14M26 6l4 -3 4 3-4 4z"/></svg>
      <h2>OUR <b>VALUES</b></h2>
    </div>
    <div class="abs value-row" style="top:74px"><div class="value-icon"><svg width="20" height="20" viewBox="0 0 20 20" fill="none" stroke="#7b3a22" stroke-width="1.6"><path d="M10 2l6 3v5c0 4-3 6-6 8-3-2-6-4-6-8V5z"/><path d="M7 10l2 2 4-4"/></svg></div><span>BE <b>SAFE</b></span></div>
    <div class="abs value-row" style="top:115px"><div class="value-icon"><svg width="20" height="20" viewBox="0 0 20 20" fill="none" stroke="#7b3a22" stroke-width="1.6"><circle cx="10" cy="7" r="4"/><path d="M3 18c1-4 4-6 7-6s6 2 7 6"/></svg></div><span>BE <b>HONEST</b></span></div>
    <div class="abs value-row" style="top:158px"><div class="value-icon"><svg width="20" height="20" viewBox="0 0 20 20" fill="none" stroke="#7b3a22" stroke-width="1.6"><circle cx="11" cy="8" r="5"/><path d="M2 16h5l4 2 7-4"/></svg></div><span>BE <b>RESPONSIBLE</b></span></div>
    <div class="abs value-row" style="top:200px"><div class="value-icon"><svg width="20" height="20" viewBox="0 0 20 20" fill="none" stroke="#7b3a22" stroke-width="1.6"><circle cx="10" cy="6" r="3"/><path d="M5 18v-4c0-2 2-4 5-4s5 2 5 4v4M3 4l1 1M17 4l-1 1"/></svg></div><span>BE <b>RESPECTFUL</b></span></div>
    <div class="abs value-row" style="top:242px"><div class="value-icon"><svg width="20" height="20" viewBox="0 0 20 20" fill="none" stroke="#7b3a22" stroke-width="1.6"><path d="M10 2l2 4 4 1-3 3 1 4-4-2-4 2 1-4-3-3 4-1z"/><path d="M4 18h12"/></svg></div><span>BE <b>GREAT</b></span></div>
  </div>

  <div class="abs fact">
    <div class="abs fact-bar">LOREM IPSUM COLOR DOLOR</div>
    <div class="abs fact-badge">FUN<br>FACT</div>
    <ul class="abs fact-list">
      <li>There are many variations of passages of Lorem Ipsum available.</li>
      <li>There are many variations of passages of Lorem Ipsum available.</li>
      <li>There are many variations of passages of Lorem Ipsum available.</li>
    </ul>
  </div>

  <h2 class="abs outlook-title">3-MONTH <b>OUTLOOK</b></h2>
  <div class="abs outlook-row" style="top:555px"><div class="date-box">JAN<br>2022</div><p>Lorem Ipsum is simply dummy text of the printing and typesetting industry. Lorem Ipsum has been the industry's standard dummy text ever since the 1500s, when an unknown printer took a galley of type.</p></div>
  <div class="abs outlook-row" style="top:623px"><div class="date-box">FEB<br>2022</div><p>Lorem Ipsum is simply dummy text of the printing and typesetting industry. Lorem Ipsum has been the industry's standard dummy text ever since the 1500s, when an unknown printer took a galley of type.</p></div>
  <div class="abs outlook-row" style="top:690px"><div class="date-box">FEB<br>2022</div><p>Lorem Ipsum is simply dummy text of the printing and typesetting industry. Lorem Ipsum has been the industry's standard dummy text ever since the 1500s, when an unknown printer took a galley of type.</p></div>

  <div class="abs employee">
    <div class="abs employee-bar">EMPLOYEE OF THE MONTH</div>
    <div class="abs employee-photo" role="img" aria-label="Photo of the employee of the month in safety gear" style="background:linear-gradient(160deg,#3a3530,#6b4a30 55%,#1e1c1a)"></div>
    <div class="abs employee-card">
      <h3>DALE BROOK</h3>
      <p>Lorem Ipsum is simply dummy text of the printing and typesetting industry. Lorem Ipsum has been the industry's standard dummy text ever since the 1500s, when an unknown printer took a galley of type. Lorem Ipsum is simply dummy text of the printing and typesetting industry. Lorem Ipsum has been the industry's standard.</p>
    </div>
  </div>
</section>

<section class="page page-two">
  <div class="abs gm" role="img" aria-label="Photo of a mine worker in a hard hat underground" style="background:linear-gradient(120deg,#7d3a24 0%,#8b4a30 50%,#a86a4c 75%,#7a3c26 100%)"></div>
  <h2 class="abs gm-title"><b>GM</b> UPDATE</h2>
  <div class="abs gm-rule"></div>
  <p class="abs gm-text">Lorem Ipsum is simply dummy text of the printing &amp; typesetting industry. Lorem Ipsum has been the industry's standard dummy text ever since the 1500s, when an unknown printer took a galley of type and scrambled it to make a type specimen book. Lorem Ipsum is simply dummy text of the printing and typesetting industry. Lorem Ipsum has been the industry's standard dummy text ever since the 1500s, when an unknown printer took a galley of typeLorem Ipsum is simply dummy text of the printing.</p>

  <h2 class="abs side-title" style="left:469px;top:39px">MONTHLY <b>TENURE</b></h2>
  <ul class="abs roster tenure">
    <li>John Smith</li><li>Kevin Doe</li><li>John Smith</li><li>Kevin Doe</li><li>John Smith</li><li>Kevin Doe</li><li>John Smith</li><li>Kevin Doe</li><li>John Smith</li><li>Kevin Doe</li>
  </ul>

  <h2 class="abs side-title" style="left:467px;top:246px">MONTHY <b>NEW HIRES</b></h2>
  <ul class="abs roster hires">
    <li>John Smith</li><li>Kevin Doe</li><li>John Smith</li><li>Kevin Doe</li><li>John Smith</li><li>Kevin Doe</li><li>John Smith</li><li>Kevin Doe</li><li>John Smith</li><li>Kevin Doe</li>
  </ul>
  <div class="abs hires-img" role="img" aria-label="Office chair with a vacant sign" style="background:radial-gradient(ellipse at 50% 45%,#2b2b2b 0%,#3a3a3a 45%,rgba(236,236,236,0) 72%)"></div>

  <div class="abs wellness">
    <h2>WELLNESS <b>FOR LIFE</b></h2>
    <div class="rule"></div>
    <p style="top:52px"><b>Lorem Ipsum</b> has been the industry's standard dummy text ever since the 1500s, when an unknown printer took a galley of type and scrambled it to make a type specimen book. Lorem Ipsum is simply dummy text of the printing and typesetting industry.</p>
    <p style="top:118px">Lorem Ipsum has been the industry's standard dummy text ever since the 1500s, when an unknown printer took a galley of type.Lorem Ipsum is simply dummy text of the <b>printing &amp; typesetting industry.</b></p>
  </div>

  <div class="abs hiring">
    <h2>WE ARE <b>HIRING</b></h2>
    <div class="abs hiring-img" role="img" aria-label="Hand holding a megaphone" style="background:radial-gradient(ellipse at 55% 40%,#f1f1f1 0%,#e3b54a 30%,rgba(217,221,221,0) 65%)"></div>
    <ul>
      <li>Lorem Ipsum is simply dummy text</li>
      <li>Lorem Ipsum is simply dummy text</li>
      <li>Lorem Ipsum is simply dummy text</li>
      <li>Lorem Ipsum is simply dummy text</li>
    </ul>
  </div>

  <h2 class="abs col-title" style="left:43px;top:652px">Community <b>Engagement</b></h2>
  <div class="abs col-rule" style="left:43px;top:678px;width:220px"></div>
  <div class="abs col-date" style="left:45px;top:692px">22.05.2022<i></i></div>
  <ul class="abs col-list" style="left:45px;top:711px;width:215px">
    <li><b>Lorem Ipsum</b> has been the industry's standard text ever since the 1500s.</li>
    <li><b>Lorem Ipsum</b> has been the industry's standard text ever since the 1500s.</li>
  </ul>
  <div class="abs col-rule" style="left:43px;top:772px;width:220px"></div>

  <h2 class="abs col-title" style="left:289px;top:652px">Upcoming <b>Holidays/Events</b></h2>
  <div class="abs col-rule" style="left:289px;top:678px;width:236px"></div>
  <div class="abs holiday-box">
    <div class="col-date">23.05.2022<i></i></div>
    <ul class="col-list">
      <li>Lorem Ipsum has been the industry's.</li>
      <li>Lorem Ipsum has been the industry's.</li>
      <li>Lorem Ipsum has been the industry's.</li>
    </ul>
  </div>

  <h2 class="abs col-title" style="left:548px;top:652px">Social <b>Club</b></h2>
  <div class="abs col-rule" style="left:548px;top:678px;width:222px"></div>
  <div class="abs col-date" style="left:550px;top:692px">24.05.2022<i></i></div>
  <ul class="abs col-list" style="left:550px;top:711px;width:215px">
    <li><b>Lorem Ipsum</b> has been the industry's standard text ever since the 1500s.</li>
    <li><b>Lorem Ipsum</b> has been the industry's standard text ever since the 1500s.</li>
  </ul>
  <div class="abs col-rule" style="left:548px;top:772px;width:222px"></div>

  <div class="abs strip">
    <svg width="727" height="168" viewBox="0 0 727 168">
      <defs>
        <linearGradient id="crew" x1="0" y1="0" x2="0" y2="1">
          <stop offset="0" stop-color="#8fb4d8"/><stop offset=".45" stop-color="#a8323a"/><stop offset="1" stop-color="#5a4a3a"/>
        </linearGradient>
      </defs>
      <rect width="727" height="168" fill="#f3bf3d"/>
      <polygon points="0,0 362,0 418,168 0,168" fill="url(#crew)" role="img" aria-label="Group photo of the mine rescue crew beside a fire truck"/>
    </svg>
    <div class="abs strip-title">UPCOMING<b>BUSINESS</b></div>

    <div class="abs cal" style="left:513px;top:7px"><h4>JANUARY</h4><div class="grid"><span>S</span><span>M</span><span>T</span><span>W</span><span>T</span><span>F</span><span>S</span><span></span><span></span><span></span><span></span><span></span><span></span><span>1</span><span>2</span><span>3</span><span>4</span><span>5</span><span>6</span><span>7</span><span>8</span><span>9</span><span>10</span><span>11</span><span>12</span><span>13</span><span>14</span><span>15</span><span>16</span><span>17</span><span>18</span><span>19</span><span>20</span><span>21</span><span>22</span><span>23</span><span>24</span><span>25</span><span>26</span><span>27</span><span>28</span><span>29</span><span>30</span><span>31</span></div></div>
    <div class="abs cal dark" style="left:613px;top:7px"><h4>FEBRUARY</h4><div class="grid"><span>S</span><span>M</span><span>T</span><span>W</span><span>T</span><span>F</span><span>S</span><span></span><span></span><span>1</span><span>2</span><span>3</span><span>4</span><span>5</span><span>6</span><span>7</span><span>8</span><span>9</span><span>10</span><span>11</span><span>12</span><span>13</span><span>14</span><span>15</span><span>16</span><span>17</span><span>18</span><span>19</span><span>20</span><span>21</span><span>22</span><span>23</span><span>24</span><span>25</span><span>26</span><span>27</span><span>28</span></div></div>
    <div class="abs cal dark" style="left:513px;top:85px"><h4>MARCH</h4><div class="grid"><span>S</span><span>M</span><span>T</span><span>W</span><span>T</span><span>F</span><span>S</span><span></span><span></span><span>1</span><span>2</span><span>3</span><span>4</span><span>5</span><span>6</span><span>7</span><span>8</span><span>9</span><span>10</span><span>11</span><span>12</span><span>13</span><span>14</span><span>15</span><span>16</span><span>17</span><span>18</span><span>19</span><span>20</span><span>21</span><span>22</span><span>23</span><span>24</span><span>25</span><span>26</span><span>27</span><span>28</span><span>29</span><span>30</span><span>31</span></div></div>
    <div class="abs cal dark" style="left:613px;top:85px"><h4>APRIL</h4><div class="grid"><span>S</span><span>M</span><span>T</span><span>W</span><span>T</span><span>F</span><span>S</span><span></span><span></span><span></span><span></span><span></span><span>1</span><span>2</span><span>3</span><span>4</span><span>5</span><span>6</span><span>7</span><span>8</span><span>9</span><span>10</span><span>11</span><span>12</span><span>13</span><span>14</span><span>15</span><span>16</span><span>17</span><span>18</span><span>19</span><span>20</span><span>21</span><span>22</span><span>23</span><span>24</span><span>25</span><span>26</span><span>27</span><span>28</span><span>29</span><span>30</span></div></div>
  </div>

  <footer class="abs footer">
    <div class="abs footer-globe"><svg width="22" height="22" viewBox="0 0 22 22" fill="none" stroke="#7b3a22" stroke-width="1.6"><circle cx="11" cy="11" r="9"/><path d="M2 11h18M11 2c3 3 3 15 0 18M11 2c-3 3-3 15 0 18"/></svg></div>
    <div class="abs footer-url">www.ravelorex.com</div>
    <div class="abs footer-follow">Follow Us</div>
    <div class="abs social" style="left:708px"></div>
    <div class="abs social" style="left:730px"></div>
    <div class="abs social" style="left:752px"></div>
  </footer>
</section>

</body>
</html>
```